VelmoraMD is an aesthetics and wellness medical spa. I am looking for a modern site, not too glam, not too boring. Currently I have the coming soon page at velmoraMD.com. The green in the logo is the accent color. I need the site to be semi neutral. I don't want it to be too geared towards females because there are some consults that men also will participate in.

```html
<!DOCTYPE html>
<html lang="en">
<head>
<meta charset="utf-8">
<title>VelmoraMD – Aesthetics and Wellness Medical Spa</title>
<link rel="stylesheet" href="https://fonts.googleapis.com/css2?family=Alegreya:wght@400;700;800&family=Alegreya+Sans:wght@400;500;700&display=swap">
<style>
:root{
  --accent:#5aa382;
  --accent-dark:#4b8f70;
  --band:#c9e0d8;
  --ink:#222;
  --body:#6b6b6b;
  --line:#e4e4e4;
  --white:#fff;
  --black:#000;
  --field:#f6f6f6;
}
*{box-sizing:border-box;margin:0;padding:0}
html,body{width:1200px;height:3757px;overflow:hidden;background:var(--white)}
body{font-family:"Alegreya Sans",sans-serif;color:var(--ink)}
.page{position:relative;width:1200px;height:3757px;overflow:hidden}
.abs{position:absolute}
.btn{position:absolute;display:flex;align-items:center;justify-content:center;border-radius:30px;font-family:"Alegreya",serif;font-weight:700;text-decoration:none}
.btn-solid{background:var(--accent);color:var(--white)}
.btn-ghost{background:var(--white);color:var(--accent);border:1.5px solid var(--accent)}

/* header */
.topline{position:absolute;left:0;top:0;width:1200px;height:6px;background:var(--band)}
.cart{left:99px;top:25px;width:156px;height:48px;font-size:20px;gap:10px}
.login{left:943px;top:25px;width:156px;height:48px;font-size:20px;gap:10px}
.brand{position:absolute;left:0;top:32px;width:1200px;font-family:"Alegreya Sans",sans-serif;font-size:30px;font-weight:500;color:#2e2e2e;display:flex;justify-content:center;align-items:center;gap:8px}
.brand-dot{width:12px;height:12px;border-radius:50%;background:var(--accent)}
.nav{position:absolute;top:99px;left:0;width:1200px;height:20px}
.nav a{position:absolute;font-size:15px;font-weight:500;color:#444;text-decoration:none;padding-left:17px}
.nav a::before{content:"";position:absolute;left:0;top:6px;width:7px;height:7px;background:var(--band)}

/* hero */
.hero-photo{left:0;top:138px;width:1200px;height:700px;background:linear-gradient(100deg,#bfc3c4 0%,#d3d6d6 35%,#c9b7a6 60%,#e7e3de 78%,#b99077 100%)}
.hero-wave{left:0;top:700px;width:1200px;height:160px}
.hero-circle{left:99px;top:299px;width:394px;height:394px;border-radius:50%;background:var(--accent);color:var(--white);text-align:center}
.hero-circle h1{position:absolute;left:40px;top:92px;width:314px;font-family:"Alegreya",serif;font-weight:400;font-size:39px;line-height:38px}
.hero-circle p{position:absolute;left:50px;top:186px;width:294px;font-size:12.5px;line-height:19px}
.hero-cta{left:120px;top:264px;width:156px;height:46px;background:var(--white);color:var(--accent);font-size:20px}

/* about */
.h2{font-family:"Alegreya",serif;font-weight:400;font-size:32px;line-height:38px;color:var(--ink)}
.h2 b{font-weight:800;letter-spacing:.5px}
.copy{font-size:11px;line-height:19.5px;color:var(--body)}
.about-title{left:99px;top:966px;width:450px}
.about-copy{left:99px;top:1062px;width:420px}
.about-copy p+p{margin-top:19.5px}
.about-btn{left:99px;top:1343px;width:123px;height:35px;font-size:14px}
.band{left:0;width:1200px;background:var(--band)}
.photo-frame{border:2px solid var(--white)}

/* why */
.why-title{left:99px;top:1543px}
.feature{position:absolute;top:1622px;width:230px}
.feature h3{display:flex;align-items:center;gap:10px;font-family:"Alegreya",serif;font-weight:500;font-size:20px;height:30px}
.feature p{margin-top:12px;font-size:10.5px;line-height:20px;color:var(--body)}
.feature a{display:block;margin-top:8px;font-size:12px;font-weight:700;color:var(--ink);text-decoration:underline}

/* services */
.services-title{left:0;top:1975px;width:1200px;text-align:center}
.card{position:absolute;top:2047px;width:320px;height:410px;background:var(--white);box-shadow:0 0 10px rgba(0,0,0,.12)}
.card-photo{position:absolute;left:9px;top:9px;width:302px;height:196px}
.card h3{position:absolute;left:31px;top:230px;font-family:"Alegreya",serif;font-weight:700;font-size:14px}
.card p{position:absolute;left:31px;top:258px;width:258px;font-size:10.5px;line-height:20px;color:var(--body)}
.card a{position:absolute;left:31px;top:368px;font-family:"Alegreya",serif;font-weight:700;font-size:13px;color:var(--accent)}

/* quote */
.quote-title{left:99px;top:2642px}
.quote-copy{left:99px;top:2694px;width:500px}
.quote-copy p+p{margin-top:19.5px}

/* contact */
.touch-title{left:0;top:3062px;width:1200px;text-align:center}
.contact-item{position:absolute;left:131px;display:flex;gap:18px;align-items:flex-start}
.contact-icon{width:50px;height:50px;border-radius:50%;background:var(--accent);display:flex;align-items:center;justify-content:center;flex:none}
.contact-item h4{font-family:"Alegreya",serif;font-weight:700;font-size:14px;color:var(--accent);margin-top:2px}
.contact-item span{display:block;font-size:11.5px;line-height:18px;color:var(--body)}
.field{position:absolute;background:var(--field);border:1px solid #eee;font-size:10.5px;color:#666;padding:18px 24px}
.submit{left:789px;top:3336px;width:280px;height:47px;font-size:14px}

/* footer */
.footer-wave{left:0;top:3440px;width:1200px;height:317px}
.foot-h{font-family:"Alegreya",serif;font-size:23px;color:var(--white);font-weight:400}
.foot-h b{font-weight:800}
.foot-links{left:99px;top:3652px;display:flex;gap:43px}
.foot-links a{color:var(--white);font-size:16px;text-decoration:none}
.copyright{left:99px;top:3697px;color:var(--white);font-size:10px}
.newsletter{left:831px;top:3651px;width:270px;height:40px;border-radius:20px;background:var(--white)}
.newsletter span{position:absolute;left:28px;top:13px;font-size:10px;color:#777}
.sub-btn{left:162px;top:1px;width:108px;height:38px;font-size:14px}
.social{top:3716px;width:22px;height:22px;border-radius:5px;background:var(--white)}
</style>
</head>
<body>
<div class="page">

  <!-- Header -->
  <div class="topline"></div>
  <a class="btn btn-ghost cart" href="#">
    <svg width="22" height="20" viewBox="0 0 22 20" fill="none" stroke="currentColor" stroke-width="1.6"><path d="M1 2h3l3 11h11l2-8H6"/><circle cx="9" cy="17" r="1.5"/><circle cx="16" cy="17" r="1.5"/></svg>
    Cart
  </a>
  <div class="brand"><span class="brand-dot"></span>VelmoraMD.</div>
  <a class="btn btn-solid login" href="#">
    <svg width="18" height="20" viewBox="0 0 18 20" fill="none" stroke="currentColor" stroke-width="1.6"><circle cx="9" cy="6" r="4.5"/><path d="M1 19c0-4.5 3.6-7 8-7s8 2.5 8 7z"/></svg>
    Login
  </a>
  <nav class="nav">
    <a href="#" style="left:99px">Home</a>
    <a href="#" style="left:243px">About Us</a>
    <a href="#" style="left:402px">Courses</a>
    <a href="#" style="left:544px">Guideliness</a>
    <a href="#" style="left:719px;top:-3px">FAQ's</a>
    <a href="#" style="left:867px">Policies</a>
    <a href="#" style="left:1011px">Contact Us</a>
  </nav>

  <!-- Hero -->
  <div class="abs hero-photo" role="img" aria-label="Photo of a client receiving a facial skin treatment from a practitioner in blue gloves"></div>
  <svg class="abs hero-wave" viewBox="0 0 1200 160" preserveAspectRatio="none" aria-hidden="true">
    <path d="M0 110 C150 50 300 50 450 85 C600 120 720 125 860 85 C980 55 1100 60 1200 72 L1200 160 L0 160Z" fill="#fff"/>
  </svg>
  <div class="abs hero-circle">
    <h1>Look and feel your best</h1>
    <p>Start or continue your aesthetics and Wellness journey here. Find out about The latest procedures, the do's and dont's, what works and what doesn't.</p>
    <a class="btn hero-cta" href="#">Get Started</a>
  </div>

  <!-- About -->
  <div class="abs band" style="top:1473px;height:444px"></div>
  <h2 class="abs h2 about-title">Aesthetics and wellness<br><b>MEDICAL SPA</b></h2>
  <div class="abs copy about-copy">
    <p>Lorem ipsum dolor sit amet, consectetur adipiscing elit, sed do eiusmod tempor incididunt ut labore et dolore magna aliqua. Quis ipsum suspendisse ultrices gravida. Risus commodo viverra maecenas accumsan lacus vel facilisis.</p>
    <p>Contrary to popular belief, Lorem Ipsum is not simply random text. It has roots in a piece of classical Latin literature from 45 BC, making it over 2000 years old. Edwin Harlow, a Latin professor at Ashford College in Virginia, looked up one of the more obscure Latin words, consectetur, from a Lorem Ipsum passage, and going through the cites of the word in classical literature, discovered the undoubtable source. Lorem Ipsum comes from sections 1.10.32 and 1.10.33 of "de Finibus Bonorum et Malorum" (The Extremes of Good and Evil) by Aurelian, written in 45 BC. This book is a treatise on the theory of ethics, very popular during the Renaissance. The first line of Lorem Ipsum, "Lorem ipsum dolor sit amet..", comes from a line in section 1.10.32.</p>
  </div>
  <a class="btn btn-solid about-btn" href="#">Learn More</a>
  <div class="abs" style="left:601px;top:907px;width:498px;height:668px;background:linear-gradient(160deg,#6e5b4c 0%,#b79a82 40%,#8a6f5c 70%,#4a3a30 100%)" role="img" aria-label="Photo of a smiling man relaxing on a massage table in a candlelit spa"></div>
  <div class="abs photo-frame" style="left:618px;top:929px;width:465px;height:622px"></div>

  <!-- Why -->
  <h2 class="abs h2 why-title">Why Choose <b>VELMORAMD</b></h2>
  <div class="feature" style="left:99px">
    <h3><svg width="28" height="28" viewBox="0 0 28 28" fill="none" stroke="#222" stroke-width="1.5"><path d="M11 26V10a2 2 0 014 0v7l7 2-1 7z"/><path d="M7 9a6 6 0 0112 0"/></svg>Instant Access</h3>
    <p>Contrary to popular belief, Lorem Ipsum is not simply random text. It has roots in a piece of classical Latin literature from 45 BC, making it over 2000 years old. Edwin Harlow, a Latin professor at Ashford College in Virginia, looked up one of the more obscure Latin words, consectetur, from a Lorem Ipsum passage, and going through the cites of the word in classical literature,</p>
    <a href="#">Read More</a>
  </div>
  <div class="feature" style="left:356px">
    <h3><svg width="28" height="28" viewBox="0 0 28 28" fill="none" stroke="#222" stroke-width="1.5"><circle cx="14" cy="14" r="5"/><circle cx="14" cy="14" r="10" stroke-dasharray="4 3"/></svg>Hassle Free</h3>
    <p>Contrary to popular belief, Lorem Ipsum is not simply random text. It has roots in a piece of classical Latin literature from 45 BC, making it over 2000 years old. Edwin Harlow, a Latin professor at Ashford College in Virginia, looked up one of the more obscure Latin words, consectetur, from a Lorem Ipsum passage, and going through the cites of the word in classical literature,</p>
    <a href="#">Read More</a>
  </div>
  <div class="feature" style="left:613px">
    <h3><svg width="28" height="28" viewBox="0 0 28 28" fill="none" stroke="#222" stroke-width="1.5"><rect x="3" y="12" width="5" height="13"/><path d="M8 13l5-9c2 0 3 1 3 3l-1 5h7a2 2 0 012 2l-2 9a2 2 0 01-2 2H8"/></svg>Risk Free</h3>
    <p>Contrary to popular belief, Lorem Ipsum is not simply random text. It has roots in a piece of classical Latin literature from 45 BC, making it over 2000 years old. Edwin Harlow, a Latin professor at Ashford College in Virginia, looked up one of the more obscure Latin words, consectetur, from a Lorem Ipsum passage, and going through the cites of the word in classical literature,</p>
    <a href="#">Read More</a>
  </div>
  <div class="feature" style="left:870px">
    <h3><svg width="28" height="28" viewBox="0 0 28 28" fill="none" stroke="#222" stroke-width="1.5"><rect x="3" y="5" width="22" height="20" rx="2"/><path d="M3 11h22M9 2v6M19 2v6"/><circle cx="19" cy="19" r="4"/><path d="M19 17v2l1.5 1"/></svg>Flexible TIming</h3>
    <p>Contrary to popular belief, Lorem Ipsum is not simply random text. It has roots in a piece of classical Latin literature from 45 BC, making it over 2000 years old. Edwin Harlow, a Latin professor at Ashford College in Virginia, looked up one of the more obscure Latin words, consectetur, from a Lorem Ipsum passage, and going through the cites of the word in classical literature,</p>
    <a href="#">Read More</a>
  </div>

  <!-- Services -->
  <h2 class="abs h2 services-title">Our <b>SERVICES</b></h2>
  <div class="card" style="left:99px">
    <div class="card-photo" style="background:linear-gradient(135deg,#3d6fd0,#c99a82 60%,#e8d8cc)" role="img" aria-label="Photo of an injection treatment on a man's forehead"></div>
    <h3>Botulinum Toxin</h3>
    <p>Contrary to popular belief, Lorem Ipsum is not simply random text. It has roots in a piece of classical Latin literature from 45 BC, making it over 2000 years old. Edwin Harlow, a Latin professor at Ashford College</p>
    <a href="#">Read More</a>
  </div>
  <div class="card" style="left:440px">
    <div class="card-photo" style="background:linear-gradient(160deg,#bfb3a8,#6a4f42 55%,#3a2a22)" role="img" aria-label="Photo of a body contouring treatment on a client lying under a brown towel"></div>
    <h3>Cryo Contouring</h3>
    <p>Contrary to popular belief, Lorem Ipsum is not simply random text. It has roots in a piece of classical Latin literature from 45 BC, making it over 2000 years old. Edwin Harlow, a Latin professor at Ashford College</p>
    <a href="#">Read More</a>
  </div>
  <div class="card" style="left:781px">
    <div class="card-photo" style="background:linear-gradient(135deg,#dfe6ee,#c79c7c 50%,#eef1f4)" role="img" aria-label="Photo of a laser hair removal device used on a leg"></div>
    <h3>Laser Hair Removal</h3>
    <p>Contrary to popular belief, Lorem Ipsum is not simply random text. It has roots in a piece of classical Latin literature from 45 BC, making it over 2000 years old. Edwin Harlow, a Latin professor at Ashford College</p>
    <a href="#">Read More</a>
  </div>
  <a class="btn btn-solid" href="#" style="left:469px;top:2490px;width:124px;height:37px;font-size:14px">View More</a>
  <a class="btn btn-ghost" href="#" style="left:607px;top:2490px;width:124px;height:37px;font-size:14px">Get Started</a>

  <!-- Quote -->
  <div class="abs band" style="top:2588px;height:360px"></div>
  <h2 class="abs h2 quote-title">Request a <b>FREE QUOTE</b></h2>
  <div class="abs copy quote-copy">
    <p>Lorem ipsum dolor sit amet, consectetur adipiscing elit, sed do eiusmod tempor incididunt ut labore et dolore magna aliqua. Quis ipsum suspendisse ultrices gravida. Risus commodo viverra maecenas accumsan lacus vel facilisis.</p>
    <p>Contrary to popular belief, Lorem Ipsum is not simply random text. It has roots in a piece of classical Latin literature from 45 BC, making it over 2000 years old. Edwin Harlow, a Latin professor at Ashford</p>
  </div>
  <a class="btn btn-solid" href="#" style="left:99px;top:2852px;width:124px;height:35px;font-size:14px">Get Started</a>
  <div class="abs" style="left:601px;top:2649px;width:497px;height:352px;background:linear-gradient(150deg,#c49a6a 0%,#7a4f33 45%,#3b2416 100%)" role="img" aria-label="Photo of a woman receiving a back scrub treatment in a spa"></div>
  <div class="abs photo-frame" style="left:614px;top:2661px;width:472px;height:328px"></div>

  <!-- Contact -->
  <h2 class="abs h2 touch-title">Get In <b>TOUCH</b></h2>
  <div class="contact-item" style="top:3136px">
    <div class="contact-icon"><svg width="20" height="24" viewBox="0 0 20 24" fill="#fff"><path d="M10 0a8 8 0 00-8 8c0 6 8 16 8 16s8-10 8-16a8 8 0 00-8-8zm0 11a3 3 0 110-6 3 3 0 010 6z"/></svg></div>
    <div><span style="margin-top:4px">453 Street Name, Place Name,<br>City Name - 87650</span></div>
  </div>
  <div class="contact-item" style="top:3206px">
    <div class="contact-icon"><svg width="22" height="22" viewBox="0 0 24 24" fill="#fff"><path d="M6.6 10.8a15 15 0 006.6 6.6l2.2-2.2c.3-.3.7-.4 1-.2 1.1.4 2.3.6 3.6.6.6 0 1 .4 1 1V20c0 .6-.4 1-1 1A17 17 0 013 4c0-.6.4-1 1-1h3.5c.6 0 1 .4 1 1 0 1.3.2 2.5.6 3.6.1.3 0 .7-.2 1z"/></svg></div>
    <div><h4>Call On</h4><span>+1 234 567 8979</span></div>
  </div>
  <div class="contact-item" style="top:3275px">
    <div class="contact-icon"><svg width="22" height="16" viewBox="0 0 22 16" fill="none" stroke="#fff" stroke-width="1.8"><rect x="1" y="1" width="20" height="14"/><path d="M1 1l10 8 10-8M1 15l7-7M21 15l-7-7"/></svg></div>
    <div><h4>Email At</h4><span>info@velmoramd.com</span></div>
  </div>
  <div class="contact-item" style="top:3343px">
    <div class="contact-icon"><svg width="22" height="22" viewBox="0 0 22 22" fill="none" stroke="#fff" stroke-width="1.6"><circle cx="11" cy="11" r="9.5"/><ellipse cx="11" cy="11" rx="4" ry="9.5"/><path d="M1.5 11h19M3 6h16M3 16h16"/></svg></div>
    <div><h4>Visit Us</h4><span>www.velmoraMD.com</span></div>
  </div>
  <div class="field" style="left:488px;top:3146px;width:280px;height:47px">First Name</div>
  <div class="field" style="left:488px;top:3211px;width:280px;height:47px">Last Name</div>
  <div class="field" style="left:488px;top:3273px;width:280px;height:47px">Phone Number</div>
  <div class="field" style="left:488px;top:3337px;width:280px;height:47px">Email Address</div>
  <div class="field" style="left:789px;top:3146px;width:280px;height:171px">Your Message Goes Here.........</div>
  <a class="btn btn-solid submit" href="#">Submit Now</a>

  <!-- Footer -->
  <svg class="abs footer-wave" viewBox="0 0 1200 317" preserveAspectRatio="none" aria-hidden="true">
    <path d="M0 40 C150 20 250 80 400 70 C550 60 650 110 800 90 C950 70 1050 30 1200 30 L1200 317 L0 317Z" fill="#000"/>
  </svg>
  <h2 class="abs foot-h" style="left:99px;top:3600px">Quick <b>LINKS</b></h2>
  <div class="abs foot-links">
    <a href="#">Home</a><a href="#">About Us</a><a href="#">Our Services</a><a href="#">Shop</a><a href="#">Contact Us</a>
  </div>
  <p class="abs copyright">Copyright © 2022 velmoramd . All Rights Reserved.</p>
  <h2 class="abs foot-h" style="left:831px;top:3600px">Join <b>WITH US</b></h2>
  <div class="abs newsletter">
    <span>Email Address</span>
    <a class="btn btn-solid sub-btn" href="#">Subscribe</a>
  </div>
  <a class="abs social" href="#" style="left:967px" aria-label="Social profile 1"></a>
  <a class="abs social" href="#" style="left:1004px" aria-label="Social profile 2"></a>
  <a class="abs social" href="#" style="left:1041px" aria-label="Social profile 3"></a>
  <a class="abs social" href="#" style="left:1079px" aria-label="Social profile 4"></a>

</div>
</body>
</html>
```